Business Card

I need a business card for a nutrition/fitness consultant. We are a personalized and online service that caters to developing individual plans based on persons needs. I will send you information to need on card as well as logo. Last business card was grey background and writing was black and red. I think a pic on the backside (maybe a photo that is on the app) would be good?

AskMarlene (Ill send you logo)
Marlene Tovak, Registered Nurse and Certified Sports Nutrionist (R.N., C.S.N.)
Personalized Nutrition and Fitness Architecture

1-800-555-0147 office
(305) 555-0182 cell
website www.askmarlene-example.com
marlene@askmarlene-example.com

Two locations so maybe two cards
2817 Willowmere Lane, inside Palmetto Glow Studio
Coral Gables, Fl 33198

and
7120 W Harbison Avenue
Boca Raton, Florida 33467

Requirements
Must have
• I guess the logo we provide so it is consistent with the new website etc

```html
<!DOCTYPE html>
<html lang="en">
<head>
<meta charset="utf-8">
<title>AskMarlene Business Cards</title>
<link rel="stylesheet" href="https://fonts.googleapis.com/css2?family=Open+Sans:wght@400;600;700&display=swap">
<style>
  :root {
    --stage-top: #8a0000;
    --stage-bottom: #2a0000;
    --card-black: #000000;
    --brand-red: #e0141b;
    --text-light: #e9e9e9;
    --text-soft: #cfcfcf;
    --logo-ink: #111111;
    --photo-light: #f2f2f2;
    --photo-mid: #bdbdbd;
    --photo-dark: #6e6e6e;
  }
  * { box-sizing: border-box; margin: 0; padding: 0; }
  html, body { width: 1014px; height: 1200px; overflow: hidden; }
  body {
    background: linear-gradient(160deg, var(--stage-top), var(--stage-bottom));
    font-family: "Open Sans", sans-serif;
    position: relative;
  }
  .card-set {
    position: absolute;
    left: 177px;
    display: flex;
    gap: 20px;
  }
  .card-set--coral-gables { top: 30px; }
  .card-set--boca-raton { top: 610px; }
  .card {
    width: 320px;
    height: 560px;
    border-radius: 26px;
    overflow: hidden;
    position: relative;
    box-shadow: 0 8px 22px rgba(0,0,0,.45);
  }
  .card--front { background: var(--photo-light); }
  .card-photo {
    position: absolute;
    inset: 0;
    background:
      radial-gradient(ellipse at 50% 80%, rgba(200,20,27,.35), transparent 45%),
      linear-gradient(170deg, var(--photo-light) 0%, var(--photo-mid) 45%, var(--photo-dark) 70%, var(--photo-light) 100%);
  }
  .front-logo {
    position: absolute;
    left: 0; right: 0;
    top: 300px;
    text-align: center;
    font-weight: 700;
    font-size: 40px;
    color: var(--logo-ink);
    letter-spacing: 1px;
  }
  .card--back {
    background: var(--card-black);
    color: var(--text-light);
    text-align: center;
    padding-top: 30px;
    letter-spacing: 1.5px;
  }
  .back-logo {
    font-weight: 700;
    font-size: 28px;
    color: var(--text-light);
    letter-spacing: 1px;
  }
  .tagline {
    margin-top: 22px;
    font-size: 14px;
    line-height: 22px;
    letter-spacing: 2px;
    text-transform: uppercase;
  }
  .person-name {
    margin-top: 22px;
    font-size: 28px;
    font-weight: 600;
    color: var(--brand-red);
    letter-spacing: 2px;
  }
  .credentials {
    margin-top: 18px;
    font-size: 15px;
    line-height: 22px;
    color: var(--text-soft);
    letter-spacing: 1.8px;
  }
  .contact-list {
    list-style: none;
    margin: 32px 0 0 16px;
    text-align: left;
    font-size: 14px;
    line-height: 29px;
    letter-spacing: .6px;
  }
  .contact-list li { display: flex; align-items: center; gap: 8px; white-space: nowrap; }
  .contact-icon { width: 14px; height: 14px; flex: none; }
  .address {
    margin-top: 26px;
    font-size: 14.5px;
    line-height: 22px;
    letter-spacing: 1.6px;
  }
</style>
</head>
<body>

<svg width="0" height="0" style="position:absolute">
  <defs>
    <symbol id="icon-mobile" viewBox="0 0 14 14">
      <rect x="3.5" y="0.8" width="7" height="12.4" rx="1.4" fill="none" stroke="#e0141b" stroke-width="1.4"/>
      <line x1="6" y1="11" x2="8" y2="11" stroke="#e0141b" stroke-width="1.2"/>
    </symbol>
    <symbol id="icon-phone" viewBox="0 0 14 14">
      <circle cx="7" cy="7" r="7" fill="#e0141b"/>
      <path d="M4.6 3.6l1.3 1.6-.8.9c.5 1.1 1.4 2 2.5 2.5l.9-.8 1.6 1.3-.9 1.3c-2.8-.4-5.1-2.7-5.5-5.5z" fill="#000"/>
    </symbol>
    <symbol id="icon-web" viewBox="0 0 14 14">
      <circle cx="7" cy="7" r="6" fill="none" stroke="#e0141b" stroke-width="1.3"/>
      <ellipse cx="7" cy="7" rx="2.6" ry="6" fill="none" stroke="#e0141b" stroke-width="1.1"/>
      <line x1="1" y1="7" x2="13" y2="7" stroke="#e0141b" stroke-width="1.1"/>
    </symbol>
    <symbol id="icon-mail" viewBox="0 0 14 14">
      <circle cx="7" cy="7" r="7" fill="#e0141b"/>
      <rect x="3.5" y="4.6" width="7" height="4.8" fill="none" stroke="#000" stroke-width="1"/>
      <path d="M3.5 4.6L7 7.4l3.5-2.8" fill="none" stroke="#000" stroke-width="1"/>
    </symbol>
  </defs>
</svg>

<section class="card-set card-set--coral-gables">
  <article class="card card--front">
    <div class="card-photo" role="img" aria-label="Black and white portrait photo of the consultant holding a red apple, with a plate of red apples in front"></div>
    <div class="front-logo">AskMarlene</div>
  </article>
  <article class="card card--back">
    <div class="back-logo">AskMarlene</div>
    <p class="tagline">Personalized Nutrition<br>&amp; Fitness Architechture</p>
    <h2 class="person-name">Marlene Tovak</h2>
    <p class="credentials">Registered Nurse and<br>Certified Sports Nutrionist</p>
    <ul class="contact-list">
      <li><svg class="contact-icon"><use href="#icon-mobile"/></svg>(305) 555-0182</li>
      <li><svg class="contact-icon"><use href="#icon-phone"/></svg>1-800-555-0147</li>
      <li><svg class="contact-icon"><use href="#icon-web"/></svg>www.askmarlene-example.com</li>
      <li><svg class="contact-icon"><use href="#icon-mail"/></svg>marlene@askmarlene-example.com</li>
    </ul>
    <p class="address">2817 Willowmere Lane,<br>inside Palmetto Glow Studio<br>Coral Gables, Fl 33198</p>
  </article>
</section>

<section class="card-set card-set--boca-raton">
  <article class="card card--front">
    <div class="card-photo" role="img" aria-label="Black and white portrait photo of the consultant holding a red apple, with a plate of red apples in front"></div>
    <div class="front-logo">AskMarlene</div>
  </article>
  <article class="card card--back">
    <div class="back-logo">AskMarlene</div>
    <p class="tagline">Personalized Nutrition<br>&amp; Fitness Architechture</p>
    <h2 class="person-name">Marlene Tovak</h2>
    <p class="credentials">Registered Nurse and<br>Certified Sports Nutrionist</p>
    <ul class="contact-list">
      <li><svg class="contact-icon"><use href="#icon-mobile"/></svg>(305) 555-0182</li>
      <li><svg class="contact-icon"><use href="#icon-phone"/></svg>1-800-555-0147</li>
      <li><svg class="contact-icon"><use href="#icon-web"/></svg>www.askmarlene-example.com</li>
      <li><svg class="contact-icon"><use href="#icon-mail"/></svg>marlene@askmarlene-example.com</li>
    </ul>
    <p class="address">7120 W Harbison Avenue<br>Boca Raton, Florida 33467</p>
  </article>
</section>

</body>
</html>
```